Enrollment Campaign

We need a flyer design for our school's enrollment campaign. Our school website is www.tbvacademy.org.

The flyer should be double sided.

I want the reader to get the following messages:
1. Montessori graduates are leading the top companies of our time.
2. We are an accredited Montessori school.
3. Enrollment is open now for all four programs:
a) Toddler: 18months (or as soon as the child is able to walk) - 3 years
b) CASA: Preschool to Senior Kindergarten (3 years to 6 years)
c) Elementary: Grades 1 to 6
d) Junior High: Grades 7 to 8
4) Our contact information:
website, email:info@tbvacademy.org, phone: 647 382 5519
5) Call for Action: Book a Tour! (there is a button on our website to book a tour)
6) In the languages punjabi, hindi and italian, I wouldn't readers to know that we offer their faith and cultural education as well.
7) Fees for children under age of 6 can be claimed in Taxes as day care expense. So, there is no reason to miss providing our children the best that we can in education.
Updates

Please note my updates to my brief in the "must have" section. Also, I have added some pics that can be used. Please note that I don't have one pic (the farming one referred to in my brief). I will really appreciate if you can kindly update your design accordingly.

Project Deadline Extended
Reason: Because of my recent update to the brief, some designers need some time to adjust their designs. I really appreciate your patience and kind consideration for my project. Thank you!

Industry/Entity Type

Education

Colors

Designer to choose colors to be used in the design.

Requirements
Must have
• Must have a unique design. I don't want a typical flyer. The design should be unique and memorable.

One of the main pics that I need is for illustrating a key feature of our new Junior High program that we are starting in August 2015. The key feature is that children are going to be operating a 'greenhouse', growing organic produce and will also be preparing their daily lunch from scratch. So, show a pic of a 13-14year old farming or something.

```html
<!DOCTYPE html>
<html lang="en">
<head>
<meta charset="utf-8">
<title>TBV Academy – Enrollment Flyer</title>
<link rel="stylesheet" href="https://fonts.googleapis.com/css2?family=Asap+Condensed:wght@600;700&family=Lato:wght@400;700&display=swap">
<style>
  :root{
    --bg:#f9d6e6;
    --magenta:#e6187f;
    --orange:#f26522;
    --lime:#c2d82f;
    --green:#6cc644;
    --teal:#2cbcc0;
    --blue:#2e86d8;
    --purple:#3a2fc8;
    --yellow:#fff200;
    --sun:#fdc33b;
    --sun-light:#ffd877;
    --white:#ffffff;
    --grey:#b8b8b8;
    --ink:#1f1f1f;
  }
  *{box-sizing:border-box;margin:0;padding:0}
  html,body{width:1200px;height:1000px;overflow:hidden}
  body{background:var(--bg);position:relative;font-family:"Lato",sans-serif}
  .page{position:absolute;top:66px;width:498px;height:846px;overflow:hidden}
  .page--front{left:92px;background:linear-gradient(180deg,var(--sun-light) 0%,var(--sun) 60%,#f9b52c 100%)}
  .page--back{left:613px;background:var(--white)}
  .page svg.shapes{position:absolute;inset:0;width:100%;height:100%}
  .photo{position:absolute}
  .headline{position:absolute;font-family:"Asap Condensed",sans-serif;font-weight:700;line-height:1.08}

  /* front */
  .hero-photo{left:28px;top:42px;width:440px;height:332px;
    background:linear-gradient(160deg,#e7e2c9 0%,#c9b48c 45%,#8b6a4f 100%)}
  .front-headline{left:42px;top:282px;font-size:22px;color:var(--yellow);transform:rotate(-6deg);transform-origin:left top;text-shadow:1px 1px 0 #8a3b0c}
  .program-photo{border:6px solid}
  .pp-toddler{left:26px;top:418px;width:104px;height:150px;border-color:var(--magenta);background:linear-gradient(160deg,#d8b79a,#8b5b4a)}
  .pp-casa{left:140px;top:405px;width:106px;height:155px;border-color:var(--blue);background:linear-gradient(160deg,#e5c9a5,#7c7fa8)}
  .pp-elem{left:253px;top:398px;width:102px;height:150px;border-color:var(--purple);background:linear-gradient(160deg,#f1e6d6,#c9a98a)}
  .pp-junior{left:363px;top:385px;width:106px;height:150px;border-color:var(--orange);background:linear-gradient(160deg,#cfc3b1,#6a6c78)}
  .program-label{position:absolute;width:106px;height:38px;display:flex;align-items:center;justify-content:center;
    font-family:"Asap Condensed",sans-serif;font-weight:700;font-size:18px;color:var(--white);transform:rotate(-4deg)}
  .pl-toddler{left:26px;top:578px;background:var(--purple)}
  .pl-casa{left:138px;top:563px;background:var(--orange)}
  .pl-elem{left:250px;top:551px;background:var(--magenta);font-size:17px}
  .pl-junior{left:362px;top:537px;background:var(--blue);font-size:17px}
  .program-note{position:absolute;width:110px;text-align:center;font-size:11px;line-height:1.4;color:#fff4d2}
  .pn-toddler{left:22px;top:622px}
  .pn-casa{left:136px;top:606px}
  .pn-elem{left:248px;top:596px}
  .pn-junior{left:360px;top:583px}
  .faith-box{position:absolute;left:263px;top:626px;width:235px;height:80px;background:var(--teal);
    clip-path:polygon(6% 0,100% 0,100% 100%,0 100%);color:var(--white);font-size:11px;line-height:1.45;padding:22px 10px 0 18px}
  .fees-note{position:absolute;left:30px;top:720px;width:440px;text-align:center;font-size:11px;line-height:1.5;color:#fff4d2}
  .contact-bar{position:absolute;left:20px;top:764px;width:460px;height:50px;display:flex;align-items:center;justify-content:space-around;
    color:var(--white);font-weight:700;font-size:15px}
  .contact-bar span{display:flex;align-items:center;gap:5px}

  /* back */
  .brand-bar{position:absolute;left:23px;top:40px;width:454px;height:62px;background:var(--white);display:flex;align-items:center;padding:0 20px}
  .brand-name{font-size:25px;color:var(--teal);font-weight:400}
  .brand-tagline{margin-left:44px;font-size:17px;font-weight:700;color:var(--green)}
  .brand-mark{margin-left:auto;width:22px;height:22px;border-radius:50%;background:var(--teal)}
  .accredited{left:196px;top:232px;font-size:34px;color:var(--white);transform:rotate(-27deg);transform-origin:left top;text-align:left;text-shadow:1px 2px 0 rgba(0,0,0,.25)}
  .enroll{left:30px;top:430px;font-size:25px;color:var(--yellow);transform:rotate(-22deg);transform-origin:left top;text-align:center;text-shadow:1px 1px 0 #5a3a00}
  .kids-photo{left:30px;top:500px;width:452px;height:282px;
    background:linear-gradient(180deg,#ffffff 0%,#f4ead9 40%,#d9a974 75%,#ffffff 100%)}
  .cta-bar{position:absolute;left:15px;top:782px;width:470px;height:21px;background:var(--magenta);color:var(--white);
    font-size:12.5px;display:flex;align-items:center;justify-content:center}
  .cta-bar b{margin:0 4px}
  .cta-sub{position:absolute;left:345px;top:808px;width:115px;font-size:9px;color:var(--grey);text-align:center}
</style>
</head>
<body>

<!-- FRONT SIDE -->
<section class="page page--front">
  <svg class="shapes" viewBox="0 0 498 846" aria-hidden="true">
    <polygon points="0,0 71,0 71,40 0,44" fill="#2f3fcf"/>
    <polygon points="71,0 142,0 142,38 71,40" fill="#e6187f"/>
    <polygon points="142,0 213,0 213,42 142,38" fill="#2cbcc0"/>
    <polygon points="213,0 284,0 284,40 213,42" fill="#6cc644"/>
    <polygon points="284,0 355,0 355,44 284,40" fill="#fff200"/>
    <polygon points="355,0 426,0 426,40 355,44" fill="#f26522"/>
    <polygon points="426,0 498,0 498,42 426,40" fill="#e6187f"/>
  </svg>

  <div class="photo hero-photo" role="img" aria-label="Photo of a smiling teacher working with three young children at a classroom table"></div>

  <svg class="shapes" viewBox="0 0 498 846" aria-hidden="true">
    <polygon points="30,290 395,262 390,350 60,384 40,340" fill="#f26522"/>
    <polygon points="392,300 472,276 468,356 388,352" fill="#2e86d8"/>
    <polygon points="30,290 60,384 48,388" fill="#b8460f"/>
    <polygon points="35,770 485,760 482,814 30,818" fill="#3f8a1f"/>
    <polygon points="22,762 478,754 480,806 20,812" fill="#6cc644"/>
  </svg>

  <p class="headline front-headline">Montessori graduates<br>are leading the top<br>companies of our time</p>

  <div class="photo program-photo pp-toddler" role="img" aria-label="Photo of a toddler at a classroom table"></div>
  <div class="photo program-photo pp-casa" role="img" aria-label="Photo of preschool children working at a table"></div>
  <div class="photo program-photo pp-elem" role="img" aria-label="Photo of an elementary student working with materials on the floor"></div>
  <div class="photo program-photo pp-junior" role="img" aria-label="Photo of junior high students working together"></div>

  <div class="program-label pl-toddler">TODDLER</div>
  <div class="program-label pl-casa">CASA</div>
  <div class="program-label pl-elem">ELEMENTARY</div>
  <div class="program-label pl-junior">JUNIOR HIGH</div>

  <p class="program-note pn-toddler">18 months<br>(or as soon as<br>the child is able<br>to walk) - 3 years</p>
  <p class="program-note pn-casa">Preschool to<br>Senior Kindergarten<br>(3 years to 6 years)</p>
  <p class="program-note pn-elem">Grades 1 to 6</p>
  <p class="program-note pn-junior">Grades 7 to 8</p>

  <p class="faith-box">In the languages Punjabi, Hindi and Italian, I wouldn't readers to know that we offer their faith and cultural education as well.</p>

  <p class="fees-note">Fees for children under age of 6 can be claimed in Taxes as day care expense.<br>So, there is no reason to miss providing our children the best that we can in education.</p>

  <div class="contact-bar">
    <span>www.tbvacademy.org</span>
    <span><svg width="16" height="12" viewBox="0 0 16 12" aria-hidden="true"><rect x="0.75" y="0.75" width="14.5" height="10.5" fill="none" stroke="#fff" stroke-width="1.5"/><polyline points="1,1 8,7 15,1" fill="none" stroke="#fff" stroke-width="1.5"/></svg>info@tbvacademy.org</span>
    <span><svg width="16" height="16" viewBox="0 0 16 16" aria-hidden="true"><circle cx="8" cy="8" r="7" fill="none" stroke="#fff" stroke-width="1.5"/><path d="M5 4.5c0 4 2.5 6.5 6.5 7l.8-1.6-2-1-1 .9c-1.3-.6-2.3-1.6-2.9-2.9l.9-1-1-2z" fill="#fff"/></svg>647 382 5519</span>
  </div>
</section>

<!-- BACK SIDE -->
<section class="page page--back">
  <svg class="shapes" viewBox="0 0 498 846" aria-hidden="true">
    <polygon points="0,0 67,0 67,470 40,462 0,472" fill="#e6187f"/>
    <polygon points="67,0 139,0 139,484 100,476 67,470" fill="#f26522"/>
    <polygon points="139,0 213,0 213,478 180,490 139,484" fill="#c2d82f"/>
    <polygon points="213,0 287,0 287,486 250,474 213,478" fill="#6cc644"/>
    <polygon points="287,0 362,0 362,476 320,482 287,486" fill="#2cbcc0"/>
    <polygon points="362,0 427,0 427,470 395,478 362,476" fill="#2e86d8"/>
    <polygon points="427,0 498,0 498,474 460,466 427,470" fill="#3a2fc8"/>
    <polygon points="180,278 468,250 222,396" fill="#f26522"/>
    <polygon points="180,278 222,396 205,402" fill="#b8460f"/>
    <polygon points="62,470 152,436 106,506" fill="#2e86d8"/>
  </svg>

  <div class="brand-bar">
    <span class="brand-name">TBV Academy</span>
    <span class="brand-tagline">Free the learning spirit</span>
    <span class="brand-mark" aria-hidden="true"></span>
  </div>

  <p class="headline accredited">An accredited<br>Montessori<br>School</p>
  <p class="headline enroll">Enrollment<br>Open</p>

  <div class="photo kids-photo" role="img" aria-label="Photo of seven smiling young children standing in a row in colourful clothes"></div>

  <p class="cta-bar">Call for Action:<b>Book a Tour !</b>(there is a button on our website to book a tour)</p>
  <p class="cta-sub">Visit tbvacademy.org today</p>
</section>

</body>
</html>
```